Managed Service Provider need new business cards

We are a small Maanged Service Provider of IT Services and need a new fresh design for our business cards. We want something impossible, fun and professional :)
Our services has a large range, but we are always fun and make sure our customers both get their issue sorted and also feel like they are "catching up with an old friend".
All our cards in the past has always been all black, with red and we need something fresher.
The back of card, we would like just a small list of what we do i think, but if someone has a better idea, please do something cool with the back of the card:
Managed IT Services
Productivity Solutions
Data Backup and Recovery
IT System Maintenance
Managed IT Security
More details can be found on our website tqnetworks.com.au
Industry/Entity Type
It Company
Contact Information for Business Card
Name: Dwayne Falstrup
Title: Director
Phone: 03 6193 4827
Mobile: 0412 587 239
Email: dwayne@tqnetworks.com.au
Web: www.tqnetworks.com.au

```html
<!DOCTYPE html>
<html lang="en">
<head>
<meta charset="utf-8">
<title>TQ Networks – Business Cards</title>
<link rel="stylesheet" href="https://fonts.googleapis.com/css2?family=Roboto:wght@400;500;700&family=Poppins:wght@300;400&display=swap">
<style>
  :root {
    --brand-red: #ec2227;
    --card-white: #ffffff;
    --ink: #333333;
    --backdrop: #e4e4e4;
  }
  * { box-sizing: border-box; margin: 0; padding: 0; }
  html, body { width: 1200px; height: 998px; overflow: hidden; }
  body {
    background: var(--backdrop);
    font-family: "Roboto", Arial, sans-serif;
    position: relative;
  }
  .card {
    position: absolute;
    left: 170px;
    width: 860px;
    height: 465px;
    overflow: hidden;
    box-shadow: 0 6px 18px rgba(0,0,0,0.18);
  }
  .card--front { top: 24px; background: var(--card-white); }
  .card--back  { top: 509px; background: var(--brand-red); }

  .wordmark {
    position: absolute;
    left: 44px;
    top: 36px;
    font-family: "Roboto", Arial, sans-serif;
    font-weight: 700;
    font-size: 46px;
    letter-spacing: 1px;
    text-transform: uppercase;
    line-height: 1;
  }
  .card--front .wordmark { color: var(--brand-red); }
  .card--back .wordmark { color: var(--card-white); }

  /* Front contact bars */
  .contact-bar {
    position: absolute;
    left: 44px;
    height: 68px;
    border-radius: 18px;
    background: var(--brand-red);
    color: var(--card-white);
    display: flex;
    align-items: center;
    font-family: "Poppins", Arial, sans-serif;
  }
  .contact-bar--name {
    top: 116px; width: 540px;
    flex-direction: column; align-items: flex-start; justify-content: center;
    padding-left: 150px;
  }
  .contact-bar--name .person { font-size: 28px; font-weight: 400; letter-spacing: 1px; text-transform: uppercase; line-height: 1.1; }
  .contact-bar--name .role { font-size: 17px; font-weight: 300; align-self: flex-end; margin-right: 60px; line-height: 1; }
  .contact-bar--phone  { top: 198px; width: 470px; padding-left: 22px; gap: 26px; font-size: 30px; }
  .contact-bar--mobile { top: 280px; width: 470px; padding-left: 150px; gap: 26px; font-size: 30px; }
  .icon { width: 34px; height: 34px; flex: none; }

  .web-details {
    position: absolute;
    right: 48px;
    top: 364px;
    text-align: left;
    font-family: "Poppins", Arial, sans-serif;
    font-size: 21px;
    line-height: 1.35;
    color: var(--ink);
  }
  .web-details .accent { color: var(--brand-red); }
  .edge-band {
    position: absolute; left: 0; right: 0; bottom: 0;
    height: 26px; background: var(--brand-red);
  }

  /* Back service list */
  .service-list {
    position: absolute;
    left: 250px;
    top: 112px;
    list-style: none;
  }
  .service-list li {
    width: 520px;
    height: 52px;
    margin-bottom: 14px;
    border: 4px solid var(--card-white);
    border-radius: 16px;
    color: var(--card-white);
    font-size: 24px;
    font-weight: 500;
    text-transform: uppercase;
    letter-spacing: 0.5px;
    display: flex;
    align-items: center;
    padding-left: 34px;
  }
  .service-list li:nth-child(2) { margin-left: 14px; }
  .service-list li:nth-child(3) { margin-left: 28px; }
  .service-list li:nth-child(4) { margin-left: 42px; }
  .service-list li:nth-child(5) { margin-left: 56px; }
</style>
</head>
<body>

<section class="card card--front" aria-label="Business card front">
  <div class="wordmark">TQ Networks</div>

  <div class="contact-bar contact-bar--name">
    <span class="person">Dwayne Falstrup</span>
    <span class="role">director</span>
  </div>

  <div class="contact-bar contact-bar--phone">
    <svg class="icon" viewBox="0 0 34 34" aria-hidden="true">
      <circle cx="17" cy="17" r="16" fill="#fff"/>
      <path d="M11 9.5c1-.8 2-.6 2.6.3l1.6 2.6c.5.8.3 1.6-.4 2.1l-1.1.8c.8 2 2.5 3.8 4.6 4.8l.8-1.1c.5-.7 1.4-.9 2.1-.4l2.6 1.6c.9.6 1 1.7.2 2.6l-1 1.1c-1 1-2.6 1.3-4 .6-4-1.9-7.1-5-9-9-.7-1.4-.4-3 .6-4z" fill="var(--brand-red)"/>
    </svg>
    <span>03 6193 4827</span>
  </div>

  <div class="contact-bar contact-bar--mobile">
    <span>0412 587 239</span>
    <svg class="icon" viewBox="0 0 34 34" aria-hidden="true">
      <rect x="2" y="2" width="30" height="30" rx="7" fill="#fff"/>
      <rect x="11" y="7" width="12" height="20" rx="2" fill="none" stroke="var(--brand-red)" stroke-width="2.4"/>
      <circle cx="17" cy="23.5" r="1.3" fill="var(--brand-red)"/>
    </svg>
  </div>

  <div class="web-details">
    <div>dwayne@tqnetworks.com.au</div>
    <div>www.<span class="accent">tqnetworks</span>.com.au</div>
  </div>

  <div class="edge-band"></div>
</section>

<section class="card card--back" aria-label="Business card back">
  <div class="wordmark">TQ Networks</div>
  <ul class="service-list">
    <li>Managed IT Services</li>
    <li>Productivity Solutions</li>
    <li>Data Backup and Recovery</li>
    <li>IT System Maintenance</li>
    <li>Managed IT Security</li>
  </ul>
</section>

</body>
</html>
```